Law Firm Website Update

I have an existing website but it is very wordy, not very aesthetically pleasing and I want additional features. I would like to update the areas of law and pictures, I would like to add a page for a client to fill in their information and links to other pages. Also want to make it more mobile friendly. site is www.tidemarklegalpc.com

Coding

Coded - Design and coding required

```html
<!DOCTYPE html>
<html lang="en">
<head>
<meta charset="utf-8">
<title>Tidemark Legal P.C. — Northern California Legal Guidance</title>
<link rel="stylesheet" href="https://fonts.googleapis.com/css2?family=Playfair+Display:wght@400;600;700&family=Poppins:wght@400;500;600&display=swap">
<style>
:root{
  --red:#d3212b;
  --red-dark:#b71b24;
  --ink:#1b1b1b;
  --text:#444;
  --muted:#777;
  --card:#efefef;
  --pink:#fbe9e9;
  --line:#d6d6d6;
  --white:#fff;
  --footer:#0f0f0f;
}
*{box-sizing:border-box;margin:0;padding:0}
html,body{width:1200px;height:5000px;overflow:hidden}
body{font-family:"Poppins",sans-serif;color:var(--text);background:var(--white);position:relative;font-size:12px}
.section-title{font-family:"Playfair Display",serif;font-weight:600;font-size:29px;color:var(--ink);text-align:center}
.btn{display:inline-flex;align-items:center;gap:10px;background:var(--red);color:var(--white);font-weight:600;font-size:15px;border-radius:5px;padding:0 22px;height:40px;white-space:nowrap}

/* header */
.topbar{position:absolute;left:583px;top:0;width:617px;height:33px;background:var(--red);display:flex;align-items:center;justify-content:flex-end;gap:48px;padding-right:60px;color:var(--white);font-size:13px}
.topbar span{display:flex;align-items:center;gap:10px}
.wordmark{font-family:"Poppins",sans-serif;font-weight:600;color:var(--red);font-size:21px;line-height:1;white-space:nowrap}
.brand{position:absolute;left:60px;top:36px}
.nav{position:absolute;right:60px;top:58px;display:flex;gap:38px;font-size:13.5px;color:var(--ink)}
.nav .active{color:var(--red);border-bottom:2px solid var(--red);padding-bottom:6px}

/* hero */
.hero{position:absolute;left:0;top:97px;width:1200px;height:524px;background:linear-gradient(180deg,#3a3f49 0%,#2b2f38 55%,#1d2028 100%)}
.hero::after{content:"";position:absolute;inset:0;background:rgba(10,12,18,.45)}
.hero-copy{position:absolute;z-index:1;left:0;right:0;top:185px;text-align:center;color:var(--white)}
.hero-copy h1{font-family:"Playfair Display",serif;font-weight:600;font-size:37px;line-height:44px}
.hero-copy p{width:440px;margin:14px auto 22px;font-size:13px;line-height:19px}

/* quote */
.quote{position:absolute;left:60px;top:621px;width:1080px;height:185px;background:var(--white);box-shadow:0 2px 12px rgba(0,0,0,.08)}
.quote h2{font-family:"Playfair Display",serif;color:var(--red);font-weight:600;font-size:27px;text-align:center;margin-top:24px}
.quote-form{position:absolute;left:22px;top:87px;display:flex;gap:14px;align-items:flex-end}
.field label{display:block;font-size:12.5px;color:var(--ink);margin-bottom:8px}
.field .input{width:211px;height:42px;border:1.5px solid var(--line);font-size:11px;color:var(--muted);padding:13px 12px}
.field:first-child .input{border-color:#999}
.quote-form .btn{width:134px;height:40px;justify-content:center;margin-bottom:1px;margin-left:2px}

/* about */
.about-title{position:absolute;top:880px;width:100%}
.about-photo{position:absolute;left:60px;top:957px;width:526px;height:383px;background:linear-gradient(135deg,#4a3426,#7b5a41 45%,#2e2520);border-right:6px solid var(--red);border-top:6px solid var(--red)}
.about-text{position:absolute;left:615px;top:970px;width:495px;font-size:12.5px;line-height:19.5px;color:var(--text)}
.about-text p{margin-bottom:10px}
.about-text .btn{margin-top:14px;font-size:14px}

/* strengths band */
.band{position:absolute;left:0;top:1416px;width:1200px;height:400px;background:linear-gradient(90deg,#17191d,#2a2a2c 50%,#17191d)}
.band h2{position:absolute;top:68px;width:100%;text-align:center;color:var(--white);font-family:"Playfair Display",serif;font-weight:600;font-size:29px;line-height:37px}
.strengths{position:absolute;left:60px;top:190px;display:flex;gap:46px}
.strength{width:320px;display:flex;gap:22px;color:var(--white)}
.strength .icon{width:58px;height:58px;background:var(--red);flex:none;display:flex;align-items:center;justify-content:center}
.strength h3{font-size:17px;font-weight:600;line-height:22px;margin-bottom:12px;width:240px}
.strength p{font-size:12px;line-height:19px;color:#ddd;width:240px}

/* practice */
.practice-title{position:absolute;top:1885px;width:100%}
.practice-grid{position:absolute;left:60px;top:1954px;width:1080px;display:grid;grid-template-columns:repeat(4,258px);gap:33px 16px}
.area{height:283px;background:var(--card);padding:18px 10px 0 18px;position:relative}
.area h3{font-size:16.5px;font-weight:600;color:var(--ink);margin-bottom:8px}
.area p{font-size:11.5px;line-height:19px;color:#666;height:58px;overflow:hidden}
.area .photo{position:absolute;left:10px;right:10px;bottom:18px;height:150px}
.area.featured{background:var(--red)}
.area.featured h3,.area.featured p{color:var(--white)}
.area .go{position:absolute;right:18px;top:100px;width:34px;height:34px;border-radius:50%;background:var(--white);display:flex;align-items:center;justify-content:center;z-index:1}

/* awards */
.awards-title{position:absolute;left:60px;top:2651px;font-family:"Playfair Display",serif;font-weight:600;font-size:29px;line-height:34px;color:var(--ink)}
.awards-arrows{position:absolute;left:60px;top:2738px;display:flex;gap:6px}
.awards-panel{position:absolute;left:344px;top:2631px;width:856px;height:166px;background:var(--pink);display:flex;align-items:center;justify-content:space-around;padding:0 30px}
.badge{background:#c9c2c2;opacity:.8}

/* reviews */
.reviews-title{position:absolute;top:2868px;width:100%}
.review-photo{position:absolute;left:260px;top:2940px;width:183px;height:183px;background:linear-gradient(135deg,#4d5a4a,#8c8a78 55%,#3c4236)}
.review-card{position:absolute;left:379px;top:2997px;width:561px;height:223px;background:var(--white);box-shadow:0 2px 12px rgba(0,0,0,.1);border-bottom:3px solid var(--red);padding:62px 30px 0 104px}
.review-card p{font-size:12.5px;line-height:20px;color:var(--ink)}
.review-card .who{font-weight:600;margin-top:6px;font-size:13.5px;color:var(--ink)}
.stars{display:flex;gap:4px;margin-top:6px}
.review-dots{position:absolute;left:974px;top:3076px;display:flex;flex-direction:column;gap:8px}
.review-dots i{width:9px;height:9px;border-radius:50%;background:#ccc;display:block}
.review-dots i.on{background:#888}

/* consult band */
.consult{position:absolute;left:0;top:3297px;width:1200px;height:350px;background:linear-gradient(90deg,#1c1c1e 0%,#2f2c2a 55%,#5c4a3e 80%,#3a302a 100%)}
.consult h2{position:absolute;left:60px;top:78px;color:var(--white);font-family:"Playfair Display",serif;font-weight:600;font-size:29px;line-height:38px}
.consult p{position:absolute;left:60px;top:168px;width:500px;color:#ddd;font-size:12.5px;line-height:19.5px}
.consult .btn{position:absolute;left:60px;top:236px}

/* attorney */
.attorney-title{position:absolute;top:3718px;width:100%}
.attorney-photo{position:absolute;left:214px;top:3793px;width:384px;height:322px;background:linear-gradient(180deg,#2b2b2b,#4a4a4a 55%,#e8e4e0 100%)}
.attorney-card{position:absolute;left:550px;top:3865px;width:388px;height:271px;background:var(--white);box-shadow:0 2px 12px rgba(0,0,0,.1);text-align:center;padding:36px 28px 0}
.attorney-card h3{font-size:17px;font-weight:600;color:var(--ink)}
.attorney-card .role{font-size:12px;font-weight:600;color:var(--ink);margin:6px 0 10px}
.attorney-card p{font-size:12px;line-height:19.5px;color:#555}
.attorney-card .btn{margin-top:14px;font-size:14px}

/* office */
.office{position:absolute;left:60px;top:4210px;width:301px;height:375px;background:var(--red);color:var(--white);padding:26px 16px}
.office h2{font-family:"Playfair Display",serif;font-weight:600;font-size:29px;margin-bottom:28px}
.office-row{display:flex;gap:16px;align-items:flex-start;margin-bottom:30px;font-size:13.5px;line-height:21px}
.office-row .ic{width:44px;height:44px;border-radius:50%;border:2px solid var(--white);flex:none;display:flex;align-items:center;justify-content:center}
.office-row .txt{padding-top:11px}
.map{position:absolute;left:361px;top:4210px;width:839px;height:375px;background:linear-gradient(135deg,#eef0f2,#e3e6ea 40%,#dfece2 75%,#cfe7d5)}

/* footer */
.footer{position:absolute;left:0;top:4661px;width:1200px;height:339px;background:var(--footer);color:#ddd}
.footer h4{color:var(--red);font-size:17px;font-weight:600;margin-bottom:12px}
.f-links{position:absolute;top:56px;font-size:12px;line-height:22.5px}
.f-links.left{left:60px}
.f-links.right{right:60px;text-align:right}
.f-center{position:absolute;left:0;right:0;top:60px;text-align:center}
.f-center p{font-size:13px;line-height:20px;margin:22px auto 16px;width:300px}
.social{display:flex;gap:8px;justify-content:center;margin-bottom:16px}
.social i{width:34px;height:34px;border-radius:50%;border:2px solid var(--red);display:block}
.f-center .btn{height:40px;width:150px;justify-content:center;font-size:14px}
.copyright{position:absolute;left:0;right:0;bottom:0;height:44px;border-top:1px solid #2a2a2a;text-align:center;font-size:12px;line-height:44px;color:#ddd}
</style>
</head>
<body>

<header>
  <div class="brand wordmark">Tidemark Legal P.C.</div>
  <div class="topbar">
    <span><svg width="16" height="16" viewBox="0 0 24 24" fill="#fff"><path d="M6.6 10.8a15 15 0 0 0 6.6 6.6l2.2-2.2c.3-.3.7-.4 1-.2 1.1.4 2.3.6 3.6.6.6 0 1 .4 1 1V20c0 .6-.4 1-1 1A17 17 0 0 1 3 4c0-.6.4-1 1-1h3.5c.6 0 1 .4 1 1 0 1.3.2 2.5.6 3.6.1.3 0 .7-.2 1z"/></svg>+ 530-555-0148</span>
    <span><svg width="18" height="14" viewBox="0 0 24 18"><path d="M1 1h22v16H1z" fill="#fff"/><path d="M1 1l11 8 11-8" stroke="#d3212b" stroke-width="2" fill="none"/></svg>info@tidemarklegal.com</span>
  </div>
  <nav class="nav">
    <span class="active">Home</span><span>About Us</span><span>Attorney Profile</span><span>Practice Areas</span><span>Review</span><span>Map</span><span>Blog</span><span>Contact</span>
  </nav>
</header>

<section class="hero" role="img" aria-label="Photo of a smiling team of attorneys in business suits">
  <div class="hero-copy">
    <h1>Northern California Legal Guidance<br>for Individuals &amp; Businesses</h1>
    <p>Providing clients with sound legal advice, fluid communication &amp; prompt service</p>
    <span class="btn"><svg width="18" height="18" viewBox="0 0 24 24" fill="#fff"><path d="M6.6 10.8a15 15 0 0 0 6.6 6.6l2.2-2.2c.3-.3.7-.4 1-.2 1.1.4 2.3.6 3.6.6.6 0 1 .4 1 1V20c0 .6-.4 1-1 1A17 17 0 0 1 3 4c0-.6.4-1 1-1h3.5c.6 0 1 .4 1 1 0 1.3.2 2.5.6 3.6.1.3 0 .7-.2 1z"/></svg>+ 530-555-0148</span>
  </div>
</section>

<section class="quote">
  <h2>Request A Quote</h2>
  <div class="quote-form">
    <div class="field"><label>Name</label><div class="input">| Your Name</div></div>
    <div class="field"><label>Email</label><div class="input">| Email Address</div></div>
    <div class="field"><label>Phone No</label><div class="input">+ 01 |</div></div>
    <div class="field"><label>Message</label><div class="input">| Your Question</div></div>
    <span class="btn">Submit</span>
  </div>
</section>

<section>
  <h2 class="section-title about-title">About Us</h2>
  <div class="about-photo" role="img" aria-label="Photo of the attorney meeting with a client in a library office"></div>
  <div class="about-text">
    <p>Tidemark Legal P.C. offers a boutique law firm option for clients who want to enjoy all the advantages of big-firm-style representation in a personal and professional environment. Out-of-the-box legal strategies that have made the seemingly impossible, possible. Our approach begins with a no-cost consultation to assess our client's needs and evaluate their position in the matter at hand. We strive to meet and exceed our firm mission to provide each and every client with sound legal advice, fluid communication and prompt service.</p>
    <p>Tidemark Legal P.C.'s CEO is Marla J. Tidwell, a dedicated and caring professional who uses her broad range of skills as a California lawyer to bring consumers and business owners exceptionally strong legal representation aimed at achieving the best results for her clients. She works with people from all over Northern California in the areas of Real Estate law, Business Law, Bankruptcy, Franchise Law and Civil Litigation.</p>
    <span class="btn">Read More</span>
  </div>
</section>

<section class="band" role="img" aria-label="Dark photo backdrop of a law office">
  <h2>Accomplished lawyer provides strong representation<br>to get clients results</h2>
  <div class="strengths">
    <div class="strength">
      <div class="icon"><svg width="36" height="36" viewBox="0 0 36 36" fill="none" stroke="#fff" stroke-width="2"><circle cx="12" cy="11" r="4"/><circle cx="24" cy="11" r="4"/><path d="M4 28c0-5 4-9 8-9s8 4 8 9M16 28c0-5 4-9 8-9s8 4 8 9"/></svg></div>
      <div><h3>One-on-one relationships<br>with clients</h3><p>Our attorney maintains reliable communication clients and gives each client dedicated</p></div>
    </div>
    <div class="strength">
      <div class="icon"><svg width="34" height="36" viewBox="0 0 34 36" fill="none" stroke="#fff" stroke-width="2"><path d="M7 3h15l6 6v24H7z"/><path d="M12 14h11M12 19h11M12 24h7"/></svg></div>
      <div><h3>Providing detailed<br>contract analysis</h3><p>Many important legal transactions rest on the terms of a contract.</p></div>
    </div>
    <div class="strength">
      <div class="icon"><svg width="38" height="36" viewBox="0 0 38 36" fill="none" stroke="#fff" stroke-width="2"><circle cx="9" cy="9" r="3.5"/><circle cx="19" cy="9" r="3.5"/><circle cx="29" cy="9" r="3.5"/><path d="M4 30V19c0-3 2-5 5-5s5 2 5 5v11M14 30V19c0-3 2-5 5-5s5 2 5 5v11M24 30V19c0-3 2-5 5-5s5 2 5 5v11"/></svg></div>
      <div><h3>Being community<br>leaders</h3><p>We pride ourselves on our extensive involvement in the business and real estate communities.</p></div>
    </div>
  </div>
</section>

<section>
  <h2 class="section-title practice-title">Practice Areas</h2>
  <div class="practice-grid">
    <div class="area"><h3>Real estate</h3><p>The purchase and sale of real estate is highly regulated at the state and national levels.</p><div class="photo" role="img" aria-label="Photo of hands reviewing documents at a desk" style="background:linear-gradient(135deg,#3a3a3a,#8a8a8a)"></div></div>
    <div class="area"><h3>Business law</h3><p>Our attorney helps companies with general business law issues, including business formation</p><div class="photo" role="img" aria-label="Photo of a business meeting around a table" style="background:linear-gradient(135deg,#6b7a88,#c8ccd0)"></div></div>
    <div class="area"><h3>Bankruptcy</h3><p>Financial difficulties can quickly overwhelm you, and bankruptcy may be the right option</p><div class="photo" role="img" aria-label="Photo of a person working at a laptop" style="background:linear-gradient(135deg,#2a2a2a,#9a958e)"></div></div>
    <div class="area featured"><h3>Dispute resolution</h3><p>We want to give our clients choices and offer representation in both civil litigation</p><span class="go"><svg width="16" height="16" viewBox="0 0 16 16"><path d="M2 8l12-6-5 12-2-5z" fill="#d3212b"/></svg></span><div class="photo" role="img" aria-label="Photo of a mediation meeting" style="background:linear-gradient(135deg,#8a6b55,#d8c6b6)"></div></div>
    <div class="area"><h3>Estate planning</h3><p>Appropriate estate planning often includes more than just drafting a will or trus</p><div class="photo" role="img" aria-label="Photo of a couple meeting with an advisor" style="background:linear-gradient(135deg,#7a6a5e,#e0d8d0)"></div></div>
    <div class="area"><h3>Franchise Law</h3><p>Franchising your business or buying into a franchise can be a lucrative business venture</p><div class="photo" role="img" aria-label="Photo of a handshake across a meeting table" style="background:linear-gradient(135deg,#4c4c52,#c4c2c0)"></div></div>
    <div class="area"><h3>Civil Litigation</h3><p>When legal disputes disrupt your business or personal life, having a committed</p><div class="photo" role="img" aria-label="Photo of a gavel on a desk" style="background:linear-gradient(135deg,#1e1e1e,#6a5a48)"></div></div>
    <div class="area"><h3>Commercial Real Estate</h3><p>The attorneys at Tidemark Legal P.C. handle all aspects of commercial real estate transactions.</p><div class="photo" role="img" aria-label="Photo of a modern glass office lobby" style="background:linear-gradient(135deg,#5e7080,#d0d8de)"></div></div>
  </div>
</section>

<section>
  <h2 class="awards-title">Awards &amp;<br>Memberships</h2>
  <div class="awards-arrows">
    <svg width="34" height="34" viewBox="0 0 34 34"><circle cx="17" cy="17" r="15.5" fill="#fff" stroke="#d3212b" stroke-width="2"/><path d="M12 11l11 6-11 6 3-6z" fill="#d3212b"/></svg>
    <svg width="34" height="34" viewBox="0 0 34 34"><circle cx="17" cy="17" r="16" fill="#d3212b"/><path d="M22 11l-11 6 11 6-3-6z" fill="#fff"/></svg>
  </div>
  <div class="awards-panel">
    <div class="badge" style="width:120px;height:36px;border-radius:4px" role="img" aria-label="Listing badge"></div>
    <div class="badge" style="width:180px;height:56px;border-radius:4px" role="img" aria-label="Foundation membership badge"></div>
    <div class="badge" style="width:92px;height:92px;border-radius:50%" role="img" aria-label="Bar association seal"></div>
    <div class="badge" style="width:190px;height:48px;border-radius:4px" role="img" aria-label="Client recognition award badge"></div>
  </div>
</section>

<section>
  <h2 class="section-title reviews-title">Reviews &amp; Ratings</h2>
  <div class="review-card">
    <p>As long as you have Tidemark Legal in your corner, justice, and freedom, are still alive. The plaintiffs against me, with thier egregious and slanderous claims, tried to cripple my freedoms on my private property.</p>
    <div class="who">- Client</div>
    <div class="stars">
      <svg width="90" height="14" viewBox="0 0 90 14" fill="#f2b705"><defs><path id="st" d="M7 0l2.1 4.6 4.9.5-3.7 3.3 1.1 4.9L7 10.8 2.6 13.3l1.1-4.9L0 5.1l4.9-.5z"/></defs><use href="#st"/><use href="#st" x="18"/><use href="#st" x="36"/><use href="#st" x="54"/><use href="#st" x="72"/></svg>
    </div>
  </div>
  <div class="review-photo" role="img" aria-label="Portrait photo of the reviewing client"></div>
  <div class="review-dots"><i></i><i></i><i class="on"></i><i></i></div>
</section>

<section class="consult" role="img" aria-label="Photo of a smiling attorney beside the consultation message">
  <h2>Contact a reliable California lawyer<br>for a free consultation</h2>
  <p>At Tidemark Legal P.C., our attorney represents clients throughout the North Sacramento Valley in real estate, business law, bankruptcy, litigation and various other matters.</p>
  <span class="btn"><svg width="18" height="18" viewBox="0 0 24 24" fill="#fff"><path d="M6.6 10.8a15 15 0 0 0 6.6 6.6l2.2-2.2c.3-.3.7-.4 1-.2 1.1.4 2.3.6 3.6.6.6 0 1 .4 1 1V20c0 .6-.4 1-1 1A17 17 0 0 1 3 4c0-.6.4-1 1-1h3.5c.6 0 1 .4 1 1 0 1.3.2 2.5.6 3.6.1.3 0 .7-.2 1z"/></svg>+ 530-555-0148</span>
</section>

<section>
  <h2 class="section-title attorney-title">Attorney Profile</h2>
  <div class="attorney-photo" role="img" aria-label="Portrait photo of attorney Marla J. Tidwell"></div>
  <div class="attorney-card">
    <h3>Marla J. Tidwell</h3>
    <div class="role">Attorney</div>
    <p>Marla Tidwell is a California real estate attorney and principal of Tidemark Legal P.C. specializing in corporate law, business law, contract law and real estate law. She is also principal and managing broker of Tidemark West Properties, a property management and real estate investment company.</p>
    <span class="btn">View More</span>
  </div>
</section>

<section>
  <div class="office">
    <h2>Office Location</h2>
    <div class="office-row"><span class="ic"><svg width="18" height="18" viewBox="0 0 24 24" fill="#fff"><path d="M6.6 10.8a15 15 0 0 0 6.6 6.6l2.2-2.2c.3-.3.7-.4 1-.2 1.1.4 2.3.6 3.6.6.6 0 1 .4 1 1V20c0 .6-.4 1-1 1A17 17 0 0 1 3 4c0-.6.4-1 1-1h3.5c.6 0 1 .4 1 1 0 1.3.2 2.5.6 3.6.1.3 0 .7-.2 1z"/></svg></span><span class="txt">+ 530-555-0148</span></div>
    <div class="office-row"><span class="ic"><svg width="20" height="18" viewBox="0 0 20 18" fill="none" stroke="#fff" stroke-width="1.8"><rect x="2" y="6" width="16" height="10" rx="1"/><path d="M5 6V2h10v4M5 10h10M5 13h6"/></svg></span><span class="txt">+ 888-555-0192</span></div>
    <div class="office-row"><span class="ic"><svg width="16" height="20" viewBox="0 0 16 20" fill="#fff"><path d="M8 0a7 7 0 0 1 7 7c0 5-7 13-7 13S1 12 1 7a7 7 0 0 1 7-7zm0 4a3 3 0 1 0 0 6 3 3 0 0 0 0-6z"/></svg></span><span class="txt">417 Orchard Lane,<br>Suite C,<br>Chico, California 95926</span></div>
  </div>
  <div class="map" role="img" aria-label="Street map of downtown Chico with the office marked"></div>
</section>

<footer class="footer">
  <div class="f-links left">
    <h4>Discover</h4>
    Home<br>About Us<br>Attorney Profile<br>Practice Areas<br>Pay Online<br>Reviews<br>Blog<br>Contact Us<br>Map &amp; Directions
  </div>
  <div class="f-center">
    <div class="wordmark">Tidemark Legal P.C.</div>
    <p>Providing clients with sound legal advice, fluid communication &amp; prompt service...</p>
    <div class="social"><i aria-label="Social profile"></i><i aria-label="Social profile"></i><i aria-label="Social profile"></i></div>
    <span class="btn">Contact Us</span>
  </div>
  <div class="f-links right">
    <h4>Practice Areas</h4>
    Real estate<br>Business law<br>Bankruptcy<br>Dispute resolution<br>Estate planning<br>Commercial Real Estate<br>Alternative Dispute Resolution<br>Civil Litigation
  </div>
  <div class="copyright">Copyright © 2025 Northgate Web Studio, LLC. All rights reserved.</div>
</footer>

</body>
</html>
```